Escape Room Flyer Design - Start up. A5

Flyer is for letterbox drops to get interest and let people know that our business exists and to a lesser extent what an escape room is. We have 1 room (the miller's shadows) and a second room coming soon (Varuna's Vault). I have attached our logo and 2 flyers that I have seen in the past that I really like the design of.
Whether you are having a night out with friends or family, celebrating a special event, planning a team-building activity, or simply wanting a diversion from the doldrums of your workweek, The Lock Box will provide you an unforgettable live-action gaming experience.

Target Market(s)

18-25

Industry/Entity Type

Entertainment

Requirements
Must have
• Logo. Phone number 0417 265 839. Website. www.thelockboxhartwell.com
Bookings essential.
Nice to have
• Mystery, a little bit on the darker side than bright colourful and blocky.
"Many Will Enter…Few Will Escape" tag line
60 minute game. Team work. 2-6 players. All ages.
Should not have
• Cartoons, characters, people

```html
<!DOCTYPE html>
<html lang="en">
<head>
<meta charset="utf-8">
<title>The Lock Box – DL Flyer</title>
<link rel="stylesheet" href="https://fonts.googleapis.com/css2?family=Archivo:wght@400;700;800&display=swap">
<style>
  :root {
    --page: #ffffff;
    --band: #111111;
    --copper: #c98237;
    --copper-deep: #b86a2c;
    --light: #ffffff;
    --text: #f2f2f2;
  }
  * { margin: 0; padding: 0; box-sizing: border-box; }
  html, body {
    width: 1200px; height: 1200px; overflow: hidden;
    background: var(--page);
  }
  .canvas {
    width: 1200px; height: 1200px;
    display: flex; align-items: center; justify-content: center;
  }
  .flyer {
    height: 1120px; width: 518px; display: block;
    box-shadow: 0 2px 8px rgba(0,0,0,0.25);
  }
  .headline {
    font-family: "Archivo", Arial, sans-serif; font-weight: 800;
    fill: var(--copper); font-size: 36px; letter-spacing: 0.5px; word-spacing: 6px;
  }
  .headline--second { fill: var(--copper-deep); }
  .body-copy { font-family: "Archivo", Arial, sans-serif; font-weight: 400; fill: var(--text); font-size: 17px; }
  .band-copy { font-family: "Archivo", Arial, sans-serif; font-weight: 400; fill: var(--light); font-size: 19px; }
  .band-copy--strong { font-weight: 700; }
  .contact { font-family: "Archivo", Arial, sans-serif; font-weight: 400; fill: var(--text); font-size: 15px; }
  .brand-name { font-family: "Archivo", Arial, sans-serif; font-weight: 700; fill: var(--copper); font-size: 24px; }
</style>
</head>
<body>
<main class="canvas">
  <svg class="flyer" viewBox="0 0 557 1205" xmlns="http://www.w3.org/2000/svg" aria-label="The Lock Box escape room flyer">
    <defs>
      <radialGradient id="bg-glow" cx="0.5" cy="0.42" r="0.75">
        <stop offset="0" stop-color="#4a4a4a"/>
        <stop offset="1" stop-color="#1d1d1d"/>
      </radialGradient>
      <radialGradient id="art-glow" cx="0.6" cy="0.45" r="0.6">
        <stop offset="0" stop-color="#d8d8d8" stop-opacity="0.85"/>
        <stop offset="0.6" stop-color="#7a7a7a" stop-opacity="0.45"/>
        <stop offset="1" stop-color="#3a3a3a" stop-opacity="0"/>
      </radialGradient>
      <linearGradient id="band-fade" x1="0" y1="0" x2="1" y2="0">
        <stop offset="0" stop-color="#1a1a1a"/>
        <stop offset="1" stop-color="#050505"/>
      </linearGradient>
      <path id="arc-one" d="M 50 322 Q 200 165 490 145"/>
      <path id="arc-two" d="M 105 358 Q 245 212 510 185"/>
    </defs>

    <!-- background -->
    <rect class="flyer__bg" width="557" height="1205" fill="url(#bg-glow)"/>

    <!-- headline -->
    <text class="headline"><textPath href="#arc-one">MANY WILL ENTER...</textPath></text>
    <text class="headline headline--second"><textPath href="#arc-two">...FEW WILL ESCAPE!</textPath></text>

    <!-- illustration area -->
    <rect class="illustration" x="270" y="320" width="270" height="420" fill="url(#art-glow)"
          role="img" aria-label="Illustration: an open doorway spilling light across a dark floor"/>

    <!-- intro copy -->
    <text class="body-copy" text-anchor="middle">
      <tspan x="178" y="477">Test your skills in</tspan>
      <tspan x="178" y="499">The Miller's Shadows</tspan>
      <tspan x="178" y="521">escape room!</tspan>
    </text>
    <g class="feature-list">
      <circle cx="94" cy="550" r="4" fill="var(--text)"/>
      <circle cx="94" cy="572" r="4" fill="var(--text)"/>
      <circle cx="94" cy="594" r="4" fill="var(--text)"/>
      <text class="body-copy">
        <tspan x="112" y="556">60 Minute game</tspan>
        <tspan x="112" y="578">2 - 6 Players</tspan>
        <tspan x="112" y="600">All ages welcome</tspan>
      </text>
    </g>

    <!-- announcement band -->
    <polygon class="band" points="0,798 557,695 557,783 0,886" fill="url(#band-fade)"/>
    <g transform="rotate(-11 280 790)">
      <text class="band-copy" x="285" y="786" text-anchor="middle">VARUNA'S VAULT ESCAPE ROOM</text>
      <text class="band-copy band-copy--strong" x="285" y="810" text-anchor="middle">COMING SOON!</text>
    </g>

    <!-- brand name -->
    <g class="brand" transform="translate(410 1030)">
      <circle cx="0" cy="-42" r="24" fill="var(--copper)"/>
      <text class="brand-name" x="0" y="8" text-anchor="middle">The Lock Box</text>
    </g>

    <!-- contact details -->
    <g class="contact-block">
      <path class="icon-phone" d="M72 1016 c2 -2 4 -2 5 0 l3 4 c1 2 0 3 -1 4 l-2 1 c1 3 3 5 6 6 l1 -2 c1 -1 3 -2 4 -1 l4 3 c2 1 2 4 0 5 l-2 2 c-6 2 -19 -10 -17 -17 z" fill="var(--text)"/>
      <g class="icon-globe" fill="none" stroke="var(--text)" stroke-width="1.4">
        <circle cx="80" cy="1052" r="8"/>
        <ellipse cx="80" cy="1052" rx="3.5" ry="8"/>
        <line x1="72" y1="1052" x2="88" y2="1052"/>
        <line x1="74" y1="1047" x2="86" y2="1047"/>
        <line x1="74" y1="1057" x2="86" y2="1057"/>
      </g>
      <text class="contact" x="104" y="1030">0417 265 839</text>
      <text class="contact" x="104" y="1057">thelockboxhartwell.com</text>
      <line x1="104" y1="1075" x2="284" y2="1075" stroke="var(--text)" stroke-width="1.2"/>
      <text class="contact" x="104" y="1098">BOOKINGS ESSENTIAL</text>
      <line x1="104" y1="1111" x2="284" y2="1111" stroke="var(--text)" stroke-width="1.2"/>
    </g>
  </svg>
</main>
</body>
</html>
```